Velvette by Marisa Holt business cards

I am after a business card that will fit the name of my business - velvette.
I want something classy and sexy and nothing tacky.
Ideas that I like are Zebra print backgrounds glitter back grounds
Two ideas I had were
1. Zebra print in black and white, the name Velvette by Marisa Holt and a shilouette of a woman laying on top of the name. Or instead of zebra a glitter background.
2. Idea very similar except for instead of a woman a pair of lips maybe a hot pink glitter or a gold glitter depending on background with the business name between the lips.
Or you can do something completely different.

Industry/Entity Type

Business

```html
<!DOCTYPE html>
<html lang="en">
<head>
<meta charset="utf-8">
<title>Velvette by Marisa Holt — Business Cards</title>
<link rel="stylesheet" href="https://fonts.googleapis.com/css2?family=Josefin+Sans:wght@300&family=Mulish:wght@400;800&display=swap">
<style>
  :root {
    --page: #ffffff;
    --silver-light: #eeeeee;
    --silver-mid: #d9d9d9;
    --silver-dark: #c4c4c4;
    --ink: #3a3a3a;
    --ink-soft: #5c5c5c;
    --rule: #8a8a8a;
    --pink: #e0117a;
    --pink-deep: #c80c6a;
    --stripe-light: #f7f7f7;
  }
  * { box-sizing: border-box; margin: 0; padding: 0; }
  html, body {
    width: 1200px; height: 873px; overflow: hidden;
    background: var(--page);
  }
  .sheet { position: relative; width: 1200px; height: 873px; }

  .card {
    position: absolute;
    background: linear-gradient(135deg, var(--silver-light) 0%, var(--silver-mid) 55%, var(--silver-dark) 100%);
    box-shadow: 0 2px 6px rgba(0,0,0,.18);
    overflow: hidden;
  }

  /* Front */
  .card--front { left: 120px; top: 160px; width: 340px; height: 560px; }
  .front__figure {
    position: absolute; left: 120px; top: 110px; width: 190px; height: 340px;
    border-radius: 40% 30% 45% 35%;
    background: linear-gradient(160deg, var(--pink) 0%, var(--pink-deep) 100%);
  }
  .front__name {
    position: absolute; left: 40px; top: 250px; width: 240px;
    font-family: "Josefin Sans", sans-serif; font-weight: 300;
    color: var(--ink);
    line-height: 1.1;
  }
  .front__name .word { display: block; font-size: 46px; letter-spacing: 2px; text-transform: uppercase; }
  .front__name .by { display: block; font-size: 22px; margin-top: 6px; padding-left: 40px; }

  /* Back */
  .card--back { left: 540px; top: 266px; width: 560px; height: 340px; }
  .back__stripes {
    position: absolute; left: 0; top: 0; width: 300px; height: 120px;
    background: linear-gradient(100deg, var(--stripe-light) 0%, rgba(247,247,247,0) 100%);
    opacity: .8;
  }
  .back__holder {
    position: absolute; right: 40px; top: 34px; text-align: right;
    font-family: "Mulish", sans-serif; color: var(--ink);
  }
  .back__holder .name { font-weight: 800; font-size: 24px; }
  .back__holder .role { font-weight: 400; font-size: 19px; color: var(--ink-soft); }
  .back__rule {
    position: absolute; left: 0; right: 0; top: 108px; height: 2px;
    background: linear-gradient(90deg, rgba(138,138,138,0) 0%, var(--rule) 40%, var(--rule) 100%);
  }
  .back__contact {
    position: absolute; left: 210px; top: 140px;
    font-family: "Mulish", sans-serif; font-weight: 400; font-size: 19px;
    color: var(--ink-soft); line-height: 1.4;
  }
  .back__contact .group { margin-bottom: 14px; }
</style>
</head>
<body>
<main class="sheet">
  <section class="card card--front" aria-label="Card front">
    <div class="front__figure" role="img" aria-label="Hot pink zebra-stripe silhouette of a reclining woman"></div>
    <h1 class="front__name"><span class="word">Velvette</span><span class="by">by Marisa Holt</span></h1>
  </section>

  <section class="card card--back" aria-label="Card back">
    <div class="back__stripes" role="img" aria-label="Faint silver zebra-stripe texture"></div>
    <div class="back__holder">
      <p class="name">Marisa Holt</p>
      <p class="role">Proprietor</p>
    </div>
    <div class="back__rule"></div>
    <address class="back__contact" style="font-style:normal">
      <div class="group">12 Larkspur Ave<br>Westbrook, CA 90412</div>
      <div class="group">555 201 4478<br>555 309 6612</div>
      <div>hello@velvettebymh.com</div>
    </address>
  </section>
</main>
</body>
</html>
```